Online-Marketing Material für Schlüsseldienst
Zielgruppe
Wir bieten einen Schlüsseldienst mit Montagen im Bereich Sicherheitstechnik sowie Öffnungen jeder Art
Aufgabenstellung
Suche ein Stimmungsbild für den Kopfbereich unter der Navigation (730x160px). Design soll zur Seite passen, bitte vorhandene URL ansehen. Bild muss auch auf auf kleinem Viewport mobile funktionieren. Die Farben sollen entsprechend passen. Es könnte auch eine Collage sein, ähnlich wie aktuell von mir selbst gemacht(kesselwerk-tuerhilfe.example), natürlich nicht so stupide. Bitte Seite mit dem Browser verkleinern um das Bild auf seine Funktionalität zu überprüfen. Thema der Collage/des Stimmungsbildes im Kopfbereich könnten Montagen, Schlüssel, Schlüssel, Einbruchschutz, Autoschlüssel, Türöffnungen, Tresoröffnungen, Notdienst oder ähnliches sein.
Außerdem brauche ich entsprechend zu dem Stimmungsbild noch ein Nexora Local Profil Cover Photo in der Größe 1024 x 576 pixels (16:9 aspect ratio). Dies soll als Titelbild für mein Local Business dienen.

```html
<!DOCTYPE html>
<html lang="de">
<head>
<meta charset="utf-8">
<title>Schlüsseldienst – Titelbild</title>
<link rel="stylesheet" href="https://fonts.googleapis.com/css2?family=Roboto+Condensed:wght@500;700;800&display=swap">
<style>
  :root {
    --teal-dark: #134f4a;
    --teal: #1c6660;
    --teal-light: #2a7a72;
    --lime: #b8d436;
    --ink: #1f2a28;
    --white: #ffffff;
    --photo-light: #c9cfd3;
    --photo-mid: #8a9aa3;
    --photo-dark: #3d4a50;
  }
  * { margin: 0; padding: 0; box-sizing: border-box; }
  html, body { width: 1200px; height: 677px; overflow: hidden; }
  body { font-family: "Roboto Condensed", "Arial Narrow", sans-serif; }

  .cover {
    position: relative;
    width: 1200px;
    height: 677px;
    overflow: hidden;
    background:
      radial-gradient(ellipse at 20% 40%, var(--teal-light) 0%, transparent 60%),
      linear-gradient(135deg, var(--teal) 0%, var(--teal-dark) 100%);
  }

  .headline { position: absolute; left: 0; top: 0; }
  .headline__plain {
    position: absolute;
    color: var(--white);
    font-weight: 700;
    text-transform: uppercase;
    white-space: nowrap;
    line-height: 1;
  }
  .headline__plain--first { left: 117px; top: 60px; font-size: 62px; }
  .headline__plain--second { left: 164px; top: 234px; font-size: 56px; }
  .headline__band {
    position: absolute;
    left: 80px;
    height: 74px;
    padding: 0 14px;
    background: var(--lime);
    color: var(--ink);
    font-weight: 800;
    font-size: 74px;
    line-height: 74px;
    text-transform: uppercase;
    white-space: nowrap;
  }
  .headline__band--first { top: 138px; width: 406px; }
  .headline__band--second { top: 306px; width: 394px; }

  .services {
    position: absolute;
    left: 64px;
    top: 452px;
    color: var(--white);
    font-weight: 500;
    font-size: 40px;
    line-height: 51px;
  }

  .tile {
    position: absolute;
    transform: translate(-50%, -50%) rotate(45deg);
    border: 9px solid var(--white);
    border-radius: 26px;
    overflow: hidden;
    box-shadow: 0 6px 18px rgba(0,0,0,0.18);
  }
  .tile__photo { width: 100%; height: 100%; }
  .tile--technician { left: 773px; top: 217px; width: 277px; height: 277px; }
  .tile--technician .tile__photo { background: linear-gradient(135deg, #f2f2f2, #dcdfe2 60%, #5c78a6); }
  .tile--cylinder { left: 1078px; top: 141px; width: 224px; height: 224px; }
  .tile--cylinder .tile__photo { background: linear-gradient(135deg, var(--photo-light), #e6e9eb 50%, #b49a84); }
  .tile--door { left: 990px; top: 469px; width: 314px; height: 314px; }
  .tile--door .tile__photo { background: linear-gradient(135deg, #4f6a86, var(--photo-mid) 50%, #c49a7c); }
  .tile--carkey { left: 686px; top: 574px; width: 240px; height: 240px; }
  .tile--carkey .tile__photo { background: linear-gradient(135deg, #9aa0a4, var(--photo-dark) 60%, #2a2f33); }

  .accent {
    position: absolute;
    transform: translate(-50%, -50%) rotate(45deg);
    background: var(--lime);
    border-radius: 9px;
  }
  .accent--top { left: 891px; top: 59px; width: 50px; height: 50px; }
  .accent--middle { left: 656px; top: 393px; width: 54px; height: 54px; }
  .accent--corner { left: 1172px; top: 627px; width: 50px; height: 50px; }
</style>
</head>
<body>
<main class="cover">
  <div class="tile tile--cylinder"><div class="tile__photo" role="img" aria-label="Hand steckt Schlüssel in einen Schließzylinder"></div></div>
  <div class="tile tile--door"><div class="tile__photo" role="img" aria-label="Monteur arbeitet an einem Türschloss"></div></div>
  <div class="tile tile--carkey"><div class="tile__photo" role="img" aria-label="Autoschlüssel mit Klappbart auf dunklem Untergrund"></div></div>
  <div class="tile tile--technician"><div class="tile__photo" role="img" aria-label="Lächelnder Handwerker mit Schraubenschlüssel"></div></div>

  <span class="accent accent--top"></span>
  <span class="accent accent--middle"></span>
  <span class="accent accent--corner"></span>

  <h1 class="headline">
    <span class="headline__plain headline__plain--first">Ihre</span>
    <span class="headline__band headline__band--first">Sicherheit</span>
    <span class="headline__plain headline__plain--second">ist unser</span>
    <span class="headline__band headline__band--second">Geschäft</span>
  </h1>

  <p class="services">Montagen, Einbruchschutz,<br>Schlüssel, Autoschlüssel,<br>Türöffnungen, u.v.m.</p>
</main>
</body>
</html>
```